Security camera surveillance warning Sign

Security Camera Sign 11" x 11" Red, Yellow and Black (White Background)
I would like a line drawing of camera image attached.
Wording: All Suspicious or Criminal Activity Will Be Reported!
WARNING
24 HOUR SURVEILLANCE

Industry/Entity Type

Security

Colors
ec1f27
000000
ffc214

Requirements
Nice to have
• I uploaded a sign and would like the new design look something like that

```html
<!DOCTYPE html>
<html lang="en">
<head>
<meta charset="utf-8">
<title>24 Hour Surveillance Warning Sign</title>
<link href="https://fonts.googleapis.com/css2?family=Roboto+Condensed:wght@700;900&display=swap" rel="stylesheet">
<style>
  :root {
    --sign-red: #ec3237;
    --sign-yellow: #ffc214;
    --sign-black: #231f20;
    --sign-white: #ffffff;
    --camera-dark: #2b2b2b;
    --camera-light: #6a6a6a;
  }
  * { margin: 0; padding: 0; box-sizing: border-box; }
  html, body {
    width: 1200px;
    height: 1200px;
    overflow: hidden;
    background: var(--sign-yellow);
    font-family: "Roboto Condensed", "Arial Narrow", sans-serif;
  }
  .sign {
    position: relative;
    width: 1200px;
    height: 1200px;
    background: var(--sign-yellow);
  }
  .sign-panel {
    position: absolute;
    left: 24px;
    top: 24px;
    width: 1152px;
    height: 1152px;
    border: 5px solid var(--sign-black);
    border-radius: 44px;
    overflow: hidden;
    background: var(--sign-white);
  }
  .band-top {
    position: absolute;
    left: 0; top: 0;
    width: 100%;
    height: 284px;
    background: var(--sign-red);
  }
  .band-bottom {
    position: absolute;
    left: 0; bottom: 0;
    width: 100%;
    height: 286px;
    background: var(--sign-red);
  }
  .notice {
    position: absolute;
    left: 0; top: 56px;
    width: 100%;
    text-align: center;
    color: var(--sign-white);
    font-weight: 700;
    font-size: 80px;
    line-height: 92px;
    letter-spacing: -0.5px;
    white-space: nowrap;
  }
  .camera-art {
    position: absolute;
    left: 271px;
    top: 320px;
    width: 640px;
    height: 430px;
    border-radius: 24px;
    background: linear-gradient(160deg, var(--camera-light) 0%, var(--camera-dark) 70%);
  }
  .warning-badge {
    position: absolute;
    left: 218px;
    top: 784px;
    width: 705px;
    height: 172px;
    background: var(--sign-yellow);
    border: 7px solid var(--sign-black);
    border-radius: 34px;
    display: flex;
    align-items: center;
    justify-content: center;
  }
  .warning-word {
    color: var(--sign-black);
    font-weight: 900;
    font-size: 158px;
    line-height: 1;
    letter-spacing: 2px;
  }
  .surveillance {
    position: absolute;
    left: 0; top: 982px;
    width: 100%;
    text-align: center;
    color: var(--sign-white);
    font-weight: 700;
    font-size: 102px;
    line-height: 1;
    letter-spacing: 1px;
    white-space: nowrap;
  }
</style>
</head>
<body>
  <main class="sign">
    <section class="sign-panel">
      <div class="band-top"></div>
      <div class="band-bottom"></div>

      <p class="notice">All Suspicious or<br>Criminal Activity Will Be Reported!</p>

      <div class="camera-art" role="img" aria-label="Line drawing of a wall-mounted security camera facing right"></div>

      <div class="warning-badge">
        <span class="warning-word">WARNING</span>
      </div>

      <p class="surveillance">24 HOUR SURVEILLANCE</p>
    </section>
  </main>
</body>
</html>
```